Freeze dried pet treats and chews packaging design

We are an Belgium based brand selling all natural treats and chews for pets. We are looking for a full color packaging design for a new line of freeze dried treats and chews for cats and dogs. The design should look familiar for our customers with our existing logo, but with a fresh new design especially for this new line. It should reflect our core values of natural, species appropriate food products without any additives or nasties.
The packaging will be a stand-up pouch with zipper, eurohole, easy open and with a window somewhere in the design to show the products inside. Please present your design as a mockup if possible.
Name of the product will be "Velmo Freeze Dried Bitzoos". Add icons to emphasize certain aspects of the product:
- 100% natural
- freeze dried (preserves all nutrients best)
- 100% mono protein
- without additives
- high in protein
- high in flavor
The design is a generic one for 12 different products, only one pouch will be produced and finished with 12 different round labels to indicate the protein source (beef, chicken, lamb, etc). You can include one of these stickers on your design to make the example complete. The sticker should have a separate color for every protein source to make it good distinguishable, an icon representing the protein source (see examples of existing packaging) and a round text around it with the protein source in text in Dutch, French and English (example: RUND - BŒUF - BEEF).
Important: after this design we need more designs for other new product lines, so the winner might get more out of this then only this one project!
High premium pet products
Petfood
- Fontastique, Roboto (used for logo and current designs), others welcome too

```html
<!DOCTYPE html>
<html lang="en">
<head>
<meta charset="utf-8">
<title>Velmo Freeze Dried Bitzoos – Pouch Front</title>
<link rel="stylesheet" href="https://fonts.googleapis.com/css2?family=Roboto:wght@400;500;700;900&display=swap">
<style>
  :root {
    --page-bg: #ffffff;
    --pouch-mint: #e1f0e6;
    --title-green: #17603d;
    --text-dark: #1d2b24;
    --brand-purple: #5b2a86;
    --grass-light: #5cbf4d;
    --grass-mid: #3fa84a;
    --grass-deep: #2f7f5a;
    --grass-shadow: #2a4a63;
    --badge-green: #1d6b43;
    --leaf-green: #4aa84a;
    --kibble-light: #d3ad79;
    --kibble-dark: #8c6338;
    --white: #ffffff;
  }
  * { margin: 0; padding: 0; box-sizing: border-box; }
  html, body {
    width: 1200px; height: 900px; overflow: hidden;
    background: var(--page-bg);
    font-family: "Roboto", Arial, sans-serif;
  }
  .pouch-front {
    position: absolute; left: 330px; top: 45px;
    width: 540px; height: 810px;
    background: var(--pouch-mint);
    overflow: hidden;
  }
  .brand-mark {
    position: absolute; top: 96px; left: 0; width: 100%;
    display: flex; justify-content: center; align-items: center; gap: 8px;
  }
  .brand-mark .dot {
    width: 14px; height: 14px; border-radius: 50%;
    background: var(--brand-purple);
  }
  .brand-mark .name {
    font-weight: 700; font-size: 32px; color: var(--brand-purple);
    letter-spacing: 0.5px;
  }
  .product-title {
    position: absolute; top: 200px; left: 0; width: 100%;
    text-align: center; color: var(--title-green);
    font-weight: 700; font-size: 61px; line-height: 63px;
    letter-spacing: -1.5px;
  }
  .claim-list {
    position: absolute; top: 356px; left: 71px;
    list-style: none; color: var(--text-dark);
    font-size: 13.5px; line-height: 20.5px;
    z-index: 4;
  }
  .claim-list li { display: flex; gap: 5px; align-items: flex-start; }
  .claim-list .tick { width: 11px; height: 11px; margin-top: 4px; flex: none; }
  .claim-list small { font-size: 9.5px; }
  .claim-list .sub { display: block; font-size: 9.5px; line-height: 11px; margin-top: -5px; padding-left: 16px; }
  .dog-art {
    position: absolute; left: 184px; top: 352px; width: 356px; height: 458px;
    background: radial-gradient(ellipse closest-side at 55% 45%,
      rgba(23,96,61,0.30) 0%, rgba(23,96,61,0.16) 55%, rgba(23,96,61,0) 100%);
    z-index: 2;
  }
  .grass-scene {
    position: absolute; left: 0; bottom: 0; width: 100%; height: 270px;
    background: linear-gradient(180deg, var(--grass-light) 0%, var(--grass-mid) 40%, var(--grass-deep) 75%, var(--grass-shadow) 100%);
    clip-path: polygon(0 4%, 20% 10%, 40% 22%, 60% 30%, 80% 26%, 100% 18%, 100% 100%, 0 100%);
    z-index: 1;
  }
  .natural-badge {
    position: absolute; left: 56px; top: 534px; width: 120px; height: 120px; z-index: 3;
  }
  .product-window {
    position: absolute; left: 243px; top: 591px; width: 194px; height: 126px;
    border-radius: 63px;
    background:
      radial-gradient(circle at 30% 40%, var(--kibble-light) 0 20%, transparent 40%),
      radial-gradient(circle at 70% 60%, var(--kibble-light) 0 18%, transparent 42%),
      linear-gradient(135deg, var(--kibble-light), var(--kibble-dark));
    z-index: 3;
  }
  .net-weight {
    position: absolute; left: 78px; top: 722px; z-index: 3;
    color: var(--white); font-size: 22px; font-weight: 400;
  }
</style>
</head>
<body>
  <main class="pouch-front">
    <div class="brand-mark">
      <span class="dot"></span>
      <span class="name">Velmo</span>
    </div>

    <h1 class="product-title">Freeze Dried<br>Bitzoos</h1>

    <ul class="claim-list">
      <li><svg class="tick" viewBox="0 0 12 12"><path d="M1 6.5 L4.5 10 L11 1.5" fill="none" stroke="#1d2b24" stroke-width="1.4"/></svg><span>Freeze dried <small>(preserves all</small></span></li>
      <li><span class="sub">nutrients best)</span></li>
      <li><svg class="tick" viewBox="0 0 12 12"><path d="M1 6.5 L4.5 10 L11 1.5" fill="none" stroke="#1d2b24" stroke-width="1.4"/></svg><span>100% mono protein</span></li>
      <li><svg class="tick" viewBox="0 0 12 12"><path d="M1 6.5 L4.5 10 L11 1.5" fill="none" stroke="#1d2b24" stroke-width="1.4"/></svg><span>Without additives</span></li>
      <li><svg class="tick" viewBox="0 0 12 12"><path d="M1 6.5 L4.5 10 L11 1.5" fill="none" stroke="#1d2b24" stroke-width="1.4"/></svg><span>High in protein</span></li>
      <li><svg class="tick" viewBox="0 0 12 12"><path d="M1 6.5 L4.5 10 L11 1.5" fill="none" stroke="#1d2b24" stroke-width="1.4"/></svg><span>High in flavor</span></li>
    </ul>

    <div class="grass-scene" role="img" aria-label="Illustrated meadow of green grass fading to deep blue-green shadows"></div>
    <div class="dog-art" role="img" aria-label="Green engraved line illustration of a dog in profile sitting in the grass"></div>

    <svg class="natural-badge" viewBox="0 0 120 120" role="img" aria-label="100% natural badge">
      <defs>
        <path id="badge-top" d="M20 60 A40 40 0 0 1 100 60"/>
        <path id="badge-bottom" d="M14 60 A46 46 0 0 0 106 60"/>
      </defs>
      <circle cx="60" cy="60" r="57" fill="#ffffff" stroke="#1d6b43" stroke-width="3"/>
      <circle cx="60" cy="60" r="30" fill="none" stroke="#1d6b43" stroke-width="1.5"/>
      <text font-family="Roboto, sans-serif" font-size="17" font-weight="500" fill="#1d6b43"><textPath href="#badge-top" startOffset="50%" text-anchor="middle">100%</textPath></text>
      <text font-family="Roboto, sans-serif" font-size="17" font-weight="500" fill="#1d6b43" letter-spacing="2"><textPath href="#badge-bottom" startOffset="50%" text-anchor="middle">NATURAL</textPath></text>
      <path d="M28 56 C45 42 75 40 98 62 C75 72 45 70 28 56 Z" fill="#4aa84a"/>
      <path d="M28 56 C50 56 75 58 98 62" stroke="#1d6b43" stroke-width="1.5" fill="none"/>
    </svg>

    <div class="product-window" role="img" aria-label="Window showing freeze dried treat pellets inside"></div>

    <p class="net-weight">200g</p>
  </main>
</body>
</html>
```